Vantor Kq Massage Gun Packaging Design

Create a packaging design for handled multi head massage gun. Here is the link to the listing for more info:https://www.trelvomart.com/product-detail/Low-Noise-Deep-Tissue-Electric-Muscle_4827391056284.html?spm=b3917.order-detail-ta-ta-b.0.0.7k42m58pqzrtW3n

Colors

Designer to choose colors to be used in the design.

Requirements
Nice to have
• I would like the see the x in "Kq" in blue color to resemble medicinal use

```html
<!DOCTYPE html>
<html lang="en">
<head>
<meta charset="utf-8">
<title>Vantor Kq Massage Gun – Box Dieline</title>
<link rel="stylesheet" href="https://fonts.googleapis.com/css2?family=Montserrat:wght@500;600;700;800;900&family=Poppins:wght@400;500;600;700&display=swap">
<style>
:root{
  --paper:#ffffff;
  --box:#0b0706;
  --cutline:#4a4a4a;
  --gold:#e3c08e;
  --gold-deep:#c99a55;
  --pill:#e6c79a;
  --text:#f3ede4;
  --muted:#cfc7bb;
  --dot:#efc25a;
}
*{margin:0;padding:0;box-sizing:border-box}
html,body{width:1200px;height:671px;overflow:hidden;background:var(--paper)}
.dieline{position:relative;width:1200px;height:671px;font-family:"Poppins",sans-serif;color:var(--text)}
.dieline svg.structure{position:absolute;left:0;top:0}
.panel{position:absolute;top:304px;height:168px;overflow:hidden}
.artwork{position:absolute;inset:0;background:
  radial-gradient(ellipse 60% 70% at 70% 45%,rgba(214,150,60,.55),transparent 70%),
  radial-gradient(ellipse 40% 30% at 75% 75%,rgba(70,160,120,.35),transparent 70%),
  var(--box)}
.brand{position:absolute;font-family:"Montserrat",sans-serif;font-weight:800;color:var(--text);letter-spacing:-.5px;white-space:nowrap;line-height:1}
.product{position:absolute;border-radius:45% 45% 40% 40%;background:radial-gradient(ellipse at 50% 35%,#8a8884,#4a4845 55%,rgba(40,38,36,0) 75%)}
.headline{position:absolute;font-family:"Montserrat",sans-serif;font-weight:900;color:var(--gold);line-height:.95;letter-spacing:-.3px}
.pill{position:absolute;background:var(--pill);color:#1a120a;font-family:"Poppins",sans-serif;font-weight:600;border-radius:0 8px 8px 0;white-space:nowrap}
.benefits h3{font-family:"Poppins",sans-serif;font-weight:700;font-size:4.6px;color:#fff;margin-top:3.4px}
.benefits p{font-size:3.1px;line-height:1.3;color:var(--muted)}
.zones{position:absolute;left:68px;top:448px;display:flex;gap:10px}
.zone{width:24px;text-align:center;font-size:1.8px;color:var(--muted)}
.zone span{display:block;width:16px;height:16px;margin:0 auto 2px;border-radius:50%;background:radial-gradient(#ddd,#777);border:.6px solid #eee}
.specs{position:absolute;left:416px;top:344px;width:180px;font-size:3.8px;color:#f1ece5}
.specs h4{font-family:"Montserrat",sans-serif;font-weight:700;font-size:4.6px;border-bottom:.4px solid #555;padding-bottom:1px;margin-bottom:3px}
.specs .row{display:grid;grid-template-columns:43px 14px 1fr;height:7.5px}
.disclaimer{position:absolute;left:416px;top:407px;font-size:2.4px;line-height:1.4;color:var(--muted)}
.mrp{position:absolute;left:417px;top:416px;width:100px;height:51px;background:#fff;border-radius:2px;color:#444;font-size:2.4px;display:flex;align-items:center;justify-content:center}
.label-box{position:absolute;left:546px;top:427px;width:56px;height:34px;background:#fff;border-radius:4px}
.keypoints{position:absolute;top:453px;display:flex;font-family:"Montserrat",sans-serif;font-weight:700;font-size:4.4px;color:#fff;white-space:nowrap}
.keypoints li{list-style:none;display:flex;align-items:center;gap:4px;position:absolute}
.keypoints li::before{content:"";width:9px;height:9px;border-radius:50%;background:var(--dot)}
.small-list{position:absolute;left:966px;font-size:3px;font-weight:600;line-height:6.9px;list-style:none;color:#fff}
.features-title{position:absolute;left:967px;top:440px;font-family:"Montserrat",sans-serif;font-weight:700;font-size:5.4px;color:#fff}
.features{position:absolute;left:966px;top:450px;display:grid;grid-template-columns:auto auto auto;column-gap:6px;row-gap:2.2px;font-size:3px;font-weight:500;color:#fff;list-style:none;white-space:nowrap}
</style>
</head>
<body>
<div class="dieline">
  <svg class="structure" width="1200" height="671" viewBox="0 0 1200 671">
    <g fill="var(--box)">
      <path d="M95 92V70a6 6 0 0 1 6-6h89a6 6 0 0 1 6 6v22z"/>
      <path d="M265 92V70a6 6 0 0 1 6-6h89a6 6 0 0 1 6 6v22z"/>
      <rect x="59" y="92" width="343" height="212"/>
      <rect x="402" y="191" width="212" height="113"/>
      <rect x="614" y="92" width="342" height="212"/>
      <rect x="956" y="191" width="212" height="113"/>
      <rect x="59" y="472" width="1109" height="133"/>
      <path d="M59 304L37 312V464L59 472z"/>
    </g>
    <path d="M172 184h42a22 22 0 0 1 32 0h42a14 14 0 0 1 0 28h-42a22 22 0 0 1-32 0h-42a14 14 0 0 1 0-28z" fill="none" stroke="#bbb" stroke-width=".5"/>
    <rect x="716" y="189" width="3" height="18" fill="none" stroke="#bbb" stroke-width=".5"/>
    <rect x="851" y="189" width="3" height="18" fill="none" stroke="#bbb" stroke-width=".5"/>
    <g stroke="#333" stroke-width=".4">
      <line x1="402" y1="304" x2="402" y2="605"/><line x1="614" y1="92" x2="614" y2="605"/><line x1="956" y1="92" x2="956" y2="605"/>
      <line x1="59" y1="304" x2="1168" y2="304"/><line x1="59" y1="472" x2="1168" y2="472"/>
    </g>
  </svg>

  <!-- Side panel: benefits -->
  <section class="panel" style="left:59px;width:343px">
    <div class="artwork" role="img" aria-label="Golden cosmic light swirl background"></div>
  </section>
  <div class="brand" style="left:76px;top:320px;font-size:26px">Vantor Kq</div>
  <div class="benefits" style="position:absolute;left:70px;top:355px;width:131px">
    <h3>Deep Tissue Muscle Relief</h3>
    <p>Vantor Kq Massage Gun is designed to deliver powerful, deep-penetrating massage to help relieve muscle soreness, stiffness, and fatigue. Ideal for daily relaxation, workout recovery, and professional use.</p>
    <h3>22-Head Massage System</h3>
    <p>Large-area multi-head design provides even pressure distribution for effective muscle relaxation and deep tissue stimulation.</p>
    <h3>Adjustable Strength Levels</h3>
    <p>Multiple intensity levels allow you to customize your massage experience—from gentle relaxation to deep muscle recovery.</p>
    <h3>High-Energy Battery Core</h3>
    <p>Built-in high-capacity battery ensures long-lasting performance for uninterrupted massage sessions.</p>
  </div>
  <div class="product" role="img" aria-label="Multi-head massage gun with digital display and 22 grey heads" style="left:211px;top:342px;width:183px;height:99px"></div>
  <div class="pill" style="left:59px;top:434px;width:82px;height:8px;font-size:4.2px;padding:1.5px 0 0 11px">Multi-Purpose Body Massage</div>
  <div class="zones">
    <div class="zone"><span role="img" aria-label="Shoulder muscles icon"></span>SHOULDER MUSCLES</div>
    <div class="zone"><span role="img" aria-label="Chest muscles icon"></span>CHEST MUSCLES</div>
    <div class="zone"><span role="img" aria-label="Back muscles icon"></span>BACK OF THE MUSCLES</div>
    <div class="zone"><span role="img" aria-label="Leg muscles icon"></span>LEG MUSCLES</div>
    <div class="zone"><span role="img" aria-label="Hip muscles icon"></span>HIP MUSCLES</div>
  </div>

  <!-- End panel: specs -->
  <section class="panel" style="left:402px;width:212px">
    <div class="artwork" role="img" aria-label="Golden and teal light streaks background" style="background:radial-gradient(ellipse 50% 60% at 90% 10%,rgba(214,150,60,.5),transparent 70%),var(--box)"></div>
  </section>
  <div class="brand" style="left:416px;top:316px;font-size:17px">Vantor Kq</div>
  <div class="specs">
    <h4>TECHNICAL SPECS</h4>
    <div class="row"><span>PRODUCT NAME</span><span>:</span><span>VANTOR KQ MASSAGE GUN</span></div>
    <div class="row"><span>MASSAGE HEADS</span><span>:</span><span>22</span></div>
    <div class="row"><span>SPEED LEVELS</span><span>:</span><span>MULTIPLE</span></div>
    <div class="row"><span>BATTERY</span><span>:</span><span>RECHARGEABLE LITHIUM BATTERY</span></div>
    <div class="row"><span>CHARGING</span><span>:</span><span>USB CHARGING</span></div>
    <div class="row"><span>MATERIAL</span><span>:</span><span>ABS + SILICONE</span></div>
    <div class="row"><span>COLOR</span><span>:</span><span>GREY</span></div>
  </div>
  <p class="disclaimer">This product is not a medical device. Do not use on injured or inflamed areas.<br>Consult a healthcare professional if you have any medical conditions.</p>
  <div class="mrp">MRP STICKER</div>
  <svg style="position:absolute;left:525px;top:445px" width="13" height="13" viewBox="0 0 24 24" fill="none" stroke="#555" stroke-width="2.4"><path d="M12 3l4 7M16 10h-5M12 3L8 10M20 18l-4-7M4 18l4-7M4 18h16"/></svg>
  <div class="label-box"></div>

  <!-- Front panel -->
  <section class="panel" style="left:614px;width:342px">
    <div class="artwork" role="img" aria-label="Golden cosmic light swirl background"></div>
  </section>
  <div class="brand" style="left:630px;top:321px;font-size:26px">Vantor Kq</div>
  <div class="headline" style="left:630px;top:374px;font-size:17.5px">MULTI-HEAD<br>DEEP TISSUE<br>MASSAGE GUN</div>
  <div class="product" role="img" aria-label="Multi-head massage gun with digital display and 22 grey heads" style="left:766px;top:344px;width:171px;height:94px"></div>
  <ul class="keypoints">
    <li style="left:626px">DEEP TISSUE MASSAGE</li>
    <li style="left:706px">22 MASSAGE HEADS</li>
    <li style="left:783px">LONG-LASTING BATTERY</li>
    <li style="left:872px">LOW NOISE TECHNOLOGY</li>
  </ul>

  <!-- End panel: features -->
  <section class="panel" style="left:956px;width:212px">
    <div class="artwork" role="img" aria-label="Golden and teal light streaks background" style="background:radial-gradient(ellipse 50% 50% at 80% 5%,rgba(214,150,60,.55),transparent 70%),radial-gradient(ellipse 30% 40% at 95% 20%,rgba(70,170,120,.35),transparent 70%),var(--box)"></div>
  </section>
  <div class="brand" style="left:969px;top:316px;font-size:17px">Vantor Kq</div>
  <div class="headline" style="left:967px;top:351px;font-size:10.6px">MULTI-HEAD<br>DEEP TISSUE<br>MASSAGE GUN</div>
  <div class="product" role="img" aria-label="Transparent view of the massage gun showing internal motor and battery" style="left:1052px;top:337px;width:96px;height:99px;border-radius:30%;background:radial-gradient(ellipse at 50% 40%,#7fae8f,#5a5c5a 55%,rgba(40,40,40,0) 78%)"></div>
  <div class="pill" style="left:956px;top:398px;width:64px;height:7px;font-size:3.6px;padding:1.3px 0 0 10px">Smart Digital Control</div>
  <ul class="small-list" style="top:406px">
    <li>• LED Display</li>
    <li>• Easy One-Touch Operation</li>
    <li>• Intelligent Speed Adjustment</li>
  </ul>
  <div class="features-title">FEATURES</div>
  <ul class="features">
    <li>• ERGONOMIC HANDHELD DESIGN</li><li>• LOW NOISE OPERATION</li><li>• PORTABLE &amp; LIGHTWEIGHT</li>
    <li>• SKIN-FRIENDLY MASSAGE HEADS</li><li>• SUITABLE FOR HOME &amp; PROFESSIONAL USE</li><li></li>
  </ul>
</div>
</body>
</html>
```